Business Card Design for Brambly Consulting

I need business cards for a new company I have started called Brambly Consulting. Brambly Consulting is a new business based out of Columbus Ohio. I will be operating in Ohio as well as nationwide. Brambly Consulting is a professional organization designed to fit your organization's specific needs. We are dedicated to the success of organizations. We handle human resource management, leadership coaching and development, executive training, team building, personality inventories and searches, performance evaluations, temp. services, custom solutions and more. Brambly consulting services a variety of industries such as government agencies, educational systems, board of directors, construction services and more, please visit our website for a full list of services (the website will be important).

I leave the design to you. I am a 45 year old male. I was in the education field for 21 years and 11 years as a superintendent. I like the colors red and black. Don't know what works, I will leave that to you as well. I would like to have it be catchy yet masculine. I have been associated with many organizations over the years both public and private, and will be reaching out to the public and private sector.

I do need a logo...so I leave that to you as well. Company name is Brambly Consulting.

Industry/Entity Type

Construction

Contact Information for Business Card

Gordon T. Brambly, President
Brambly Consulting
47 W.Elmcrest Ave. Suite 318
Arcade at Wexbury Court
Columbus, Ohio 43287

Phone : 330-555-0193
email : gbrambly@bramblyadvisors.example
web : www.bramblyadvisors.example
twitter : @bramblyadvisors
facebook : Brambly Consulting

```html
<!DOCTYPE html>
<html lang="en">
<head>
<meta charset="utf-8">
<title>Brambly Consulting – Business Card</title>
<link rel="stylesheet" href="https://fonts.googleapis.com/css2?family=Open+Sans:wght@400;600;700&display=swap">
<style>
  :root {
    --red: #c8102e;
    --red-deep: #8e0b20;
    --black: #111111;
    --white: #ffffff;
  }
  html, body {
    margin: 0;
    padding: 0;
    width: 1200px;
    height: 688px;
    overflow: hidden;
    background: var(--white);
  }
  .card {
    position: relative;
    width: 1200px;
    height: 688px;
    overflow: hidden;
    background: var(--white);
    font-family: "Open Sans", Arial, sans-serif;
    color: var(--black);
  }
  .band-top {
    position: absolute;
    left: 0; top: 0;
    width: 1200px; height: 15px;
    background: var(--black);
  }
  .band-divider {
    position: absolute;
    left: 0; top: 368px;
    width: 1200px; height: 14px;
    background: var(--black);
  }
  .panel-contact {
    position: absolute;
    left: 0; top: 405px;
    width: 1200px; height: 283px;
    background: var(--red);
  }
  .brand-mark {
    position: absolute;
    left: 110px; top: 86px;
    width: 165px; height: 165px;
    background: linear-gradient(135deg, var(--red), var(--red-deep));
  }
  .brand-name {
    position: absolute;
    left: 32px; top: 290px;
    margin: 0;
    font-size: 32px;
    font-weight: 700;
    letter-spacing: -0.5px;
    line-height: 1;
  }
  .person {
    position: absolute;
    left: 649px; top: 172px;
    margin: 0;
  }
  .person-name {
    display: block;
    font-size: 33px;
    font-weight: 700;
    line-height: 1;
    letter-spacing: -0.3px;
  }
  .person-title {
    display: block;
    margin: 6px 0 0 65px;
    font-size: 33px;
    font-weight: 400;
    line-height: 1;
  }
  .contact-line {
    position: absolute;
    left: 80px;
    display: flex;
    align-items: center;
    gap: 14px;
    margin: 0;
    font-size: 27px;
    line-height: 1;
    color: var(--white);
  }
  .contact-phone { top: 470px; font-size: 34px; }
  .contact-email { top: 550px; }
  .contact-web { top: 606px; }
  .contact-line svg { flex: none; }
  .address {
    position: absolute;
    left: 722px; top: 428px;
    margin: 0;
    font-style: normal;
    font-size: 32px;
    line-height: 55px;
    color: var(--white);
  }
</style>
</head>
<body>
  <main class="card">
    <div class="band-top"></div>

    <div class="brand-mark" aria-hidden="true"></div>
    <h1 class="brand-name">Brambly Consulting</h1>

    <p class="person">
      <span class="person-name">Gordon T. Brambly</span>
      <span class="person-title">President</span>
    </p>

    <div class="band-divider"></div>

    <section class="panel-contact" aria-label="Contact details"></section>

    <p class="contact-line contact-phone">
      <svg width="40" height="60" viewBox="0 0 40 60" aria-hidden="true">
        <rect x="10" y="0" width="7" height="12" rx="2" fill="#ffffff"/>
        <rect x="2" y="9" width="36" height="50" rx="8" fill="#ffffff"/>
        <rect x="9" y="17" width="22" height="16" rx="2" fill="#c8102e"/>
        <rect x="9" y="39" width="22" height="12" rx="2" fill="#c8102e"/>
      </svg>
      <span>- 330-555-0193</span>
    </p>

    <p class="contact-line contact-email">
      <svg width="40" height="30" viewBox="0 0 42 30" aria-hidden="true">
        <rect x="2" y="2" width="38" height="26" fill="none" stroke="#ffffff" stroke-width="3"/>
        <path d="M2 2 L21 17 L40 2 M2 28 L16 13 M40 28 L26 13" fill="none" stroke="#ffffff" stroke-width="3"/>
      </svg>
      <span>- gbrambly@bramblyadvisors.example</span>
    </p>

    <p class="contact-line contact-web">
      <svg width="40" height="32" viewBox="0 0 32 32" aria-hidden="true">
        <circle cx="16" cy="16" r="13" fill="none" stroke="#ffffff" stroke-width="2.5"/>
        <ellipse cx="16" cy="16" rx="6" ry="13" fill="none" stroke="#ffffff" stroke-width="2"/>
        <path d="M3 16 H29 M5 9 H27 M5 23 H27" fill="none" stroke="#ffffff" stroke-width="2"/>
      </svg>
      <span>- www.bramblyadvisors.example</span>
    </p>

    <address class="address">
      47 W.Elmcrest Ave,<br>
      Suite 318 Arcade at<br>
      Wexbury Court Columbus,<br>
      Ohio 43287
    </address>
  </main>
</body>
</html>
```